Visitenkarten-Design Neutrale Verzollungs Agentur für den Grenzverkehr des Zollwesens
Sehr schnelle Umsetzung nach unserer Vorstellung,und sehr netter und guter Umgang in der Kominikation. tolvex hat unsere erwartung zu 100 % übertroffen.
Zielgruppe
Wir sind eine Neutrale Verzollungs Agentur für den Grenzverkehr des Zollwesens
Bluefen & Marlow Group
Wir führen für Kunden die Zollabwicklungen ab.
Seefracht - Bahnfracht-Luftfracht-LKW Fracht
Cargo - Hersteller Firmen und Endknden International
Aufgabenstellung
Rückseite sollte mitgestaltet werden

```html
<!DOCTYPE html>
<html lang="de">
<head>
<meta charset="utf-8">
<title>Veldmark – Visitenkarte</title>
<link rel="stylesheet" href="https://fonts.googleapis.com/css2?family=Open+Sans:wght@600&family=Quicksand:wght@700&family=Questrial&display=swap">
<style>
  :root {
    --backdrop: #c8c8c8;
    --paper: #ffffff;
    --ink-grey: #454545;
    --ink-soft: #3a3a3a;
    --brand-blue: #3f88c9;
    --rule-blue: #8fb3d6;
    --stripe: #ebebf3;
    --back-teal: #2f7f9e;
    --back-navy: #0c3c74;
    --globe-light: #5fa3a2;
    --globe-mid: #2e6f99;
    --logo-light: #c9daf0;
  }
  * { margin: 0; padding: 0; box-sizing: border-box; }
  html, body { width: 1073px; height: 1200px; overflow: hidden; background: var(--backdrop); }
  .canvas { position: relative; width: 1073px; height: 1200px; }

  .card { position: absolute; overflow: hidden; }
  .card--front {
    left: 140px; top: 142px; width: 791px; height: 455px;
    background: var(--paper);
    box-shadow: 1px 2px 4px rgba(0,0,0,.35);
  }
  .card--back {
    left: 144px; top: 658px; width: 787px; height: 456px;
    background: linear-gradient(90deg, var(--back-teal) 0%, #22638f 50%, var(--back-navy) 85%);
  }

  .stripes { position: absolute; left: 0; top: 36px; width: 100%; height: 104px; }
  .stripes span { display: block; height: 2px; background: var(--stripe); margin-bottom: 8px; }
  .logo-plate {
    position: absolute; left: 90px; top: 70px; width: 260px; height: 82px;
    background: var(--paper); border-radius: 40px;
  }
  .brand-name {
    position: absolute; font-family: "Open Sans", sans-serif; font-weight: 600;
    white-space: nowrap; letter-spacing: .5px;
  }
  .card--front .brand-name { left: 104px; top: 92px; font-size: 34px; color: var(--ink-grey); }
  .countries {
    position: absolute; left: 390px; top: 124px;
    font-family: "Open Sans", sans-serif; font-weight: 600; font-size: 14.5px; color: var(--ink-grey);
  }

  .company {
    position: absolute; right: 468px; top: 254px; text-align: right;
    font-family: "Quicksand", sans-serif; font-weight: 700; font-size: 20px; line-height: 24px;
    color: var(--brand-blue);
  }
  .address {
    position: absolute; right: 468px; top: 335px; text-align: right;
    font-family: "Questrial", sans-serif; font-size: 19px; line-height: 25px; color: var(--ink-soft);
  }
  .divider { position: absolute; left: 381px; top: 251px; width: 1px; height: 165px; background: var(--rule-blue); }
  .contact {
    position: absolute; left: 449px; font-family: "Questrial", sans-serif;
    font-size: 19px; line-height: 24.5px; color: var(--ink-soft);
  }
  .contact--phone { top: 266px; }
  .contact--web { top: 340px; }

  .globe-art {
    position: absolute; left: 36px; top: -28px; width: 524px; height: 524px; border-radius: 50%;
    background: radial-gradient(circle at 42% 52%, var(--globe-light) 0%, var(--globe-mid) 55%, rgba(30,90,140,.4) 100%);
  }
  .card--back .brand-name { left: 426px; top: 180px; font-size: 42px; color: var(--logo-light); }
</style>
</head>
<body>
<main class="canvas">
  <section class="card card--front">
    <div class="stripes"><span></span><span></span><span></span><span></span><span></span><span></span><span></span><span></span><span></span><span></span></div>
    <div class="logo-plate"></div>
    <div class="brand-name">Veldmark</div>
    <p class="countries">Switzerland · Germany · Denmark · France</p>

    <p class="company">Bluefen &amp; Marlow<br>Group GmbH</p>
    <p class="address">Birkenweg 52<br>A-3810 Lindhofen</p>
    <div class="divider"></div>
    <p class="contact contact--phone">Tel: 02717/480 63-14<br>Fax: 02717/480 63-19</p>
    <p class="contact contact--web">E-mail: service@veldmark-zoll.com<br>Web: www.veldmark-zoll.com</p>
  </section>

  <section class="card card--back">
    <div class="globe-art" role="img" aria-label="Globus mit Längen- und Breitengraden, Nord- und Südamerika in Dunkelblau"></div>
    <div class="brand-name">Veldmark</div>
  </section>
</main>
</body>
</html>
```